Automotive Parts Company Business Card/Logo Design

We need a logo/business card for a new automotive parts and accessories company which is based in Barbados. The company will only have an online presence and this will reduce our overheads and allow us to pass potential savings to our customers.

We will offer most automotive parts which include, but are not limited to, accessories, exterior, interior, body parts.

We want to appeal to a very wide audience and we're looking for a modern, clean and bold design to make the company seem very professional. Our logo and facebook page will be our only customer facing items. So it is essential that these are done correctly.

The design should really communicate that we can provide premium car parts at affordable prices for all types of cars e.g. European and Japanese.

We will stock items and also source hard to get and unique pieces. We aim to not just be another shop that sells parts. But we want to work with our customers to achieve their car goals.

The company name is GearNest and our slogan is Quality Parts At Affordable Prices.
The design should be very modern, clean and bold.

I've included examples of some of the business cards I like as well as images of car products.
Updates

Dear Designers,

I've uploaded some samples of some business card/logo designs I like. Please have a look at the project brief. Just to reiterate, I am looking for a clean, modern design.

Thanks,

Rohan

Dear Designers,

Please note the Apr 14th deadline is soon approaching.

Also note the business card is double-sided.

I look forward to working with you.

Thanks,

Rohan

Target Market(s)

20 - 30 (young professionals, younger generation with disposible income) and then then all other markets

Industry/Entity Type

Automotive

Contact Information for Business Card

Rohan Mehtabrooke
GearNest
Quality Parts At Affordable Prices
https://www.example-social.test/gearnestbb
246-555-0192
gearnestbb@mailbox-demo.test

```html
<!DOCTYPE html>
<html lang="en">
<head>
<meta charset="utf-8">
<title>GearNest Business Cards</title>
<link rel="stylesheet" href="https://fonts.googleapis.com/css2?family=Exo+2:ital,wght@0,400;0,700;1,400&display=swap">
<style>
  :root{
    --stage:#1c1c1e;
    --card:#141414;
    --card-light:#1e1e1e;
    --band:#0e0e0e;
    --gold:#e2b24a;
    --white:#f2f2f2;
    --photo-dark:#0b0b0b;
    --photo-mid:#5a5a5c;
    --photo-light:#c9c9cb;
  }
  *{box-sizing:border-box;margin:0;padding:0}
  html,body{width:1200px;height:900px;overflow:hidden}
  body{
    background:var(--stage);
    font-family:"Exo 2",Arial,sans-serif;
    color:var(--white);
    position:relative;
  }
  .card{
    position:absolute;width:503px;height:286px;overflow:hidden;
    background:linear-gradient(180deg,var(--card-light),var(--card));
    box-shadow:0 6px 18px rgba(0,0,0,.55);
  }
  .card--front{left:85px;top:152px}
  .card--back{left:612px;top:152px}
  .card--gauge{left:85px;top:463px}
  .card--alt{left:612px;top:463px}

  .wheel-photo{
    position:absolute;left:0;top:0;width:100%;height:150px;
    background:linear-gradient(90deg,var(--photo-dark) 0%,var(--photo-mid) 35%,var(--photo-light) 60%,var(--photo-mid) 80%,var(--photo-dark) 100%);
  }
  .wheel-photo::after{
    content:"";position:absolute;inset:0;
    background:linear-gradient(180deg,rgba(0,0,0,0) 55%,rgba(0,0,0,.8) 100%);
  }
  .card--alt .wheel-photo{height:152px}

  .wordmark{
    position:absolute;font-weight:700;color:var(--gold);
    letter-spacing:-.5px;line-height:1;white-space:nowrap;
  }
  .slogan{
    position:absolute;font-style:italic;font-size:10px;color:var(--gold);white-space:nowrap;
  }

  .card--front .wordmark{right:33px;top:50px;font-size:38px}
  .card--front .slogan{right:36px;top:92px}
  .holder-name{
    position:absolute;right:36px;top:190px;font-size:18px;font-style:italic;color:var(--gold);
  }
  .contact{position:absolute;font-size:13px;line-height:16px;white-space:nowrap}
  .contact .label{color:var(--gold);font-style:italic}
  .card--front .contact{font-size:12px}
  .card--front .phone{right:36px;top:223px}
  .card--front .email{right:36px;top:241px}
  .card--front .web{left:28px;top:241px}
  .web{font-style:italic;color:var(--gold)}
  .web b{font-weight:400;color:var(--white);font-style:normal}

  .card--back .band{
    position:absolute;left:0;top:90px;width:100%;height:108px;background:var(--band);
  }
  .card--back .wordmark{left:0;right:0;text-align:center;top:115px;font-size:46px}
  .card--back .slogan{left:0;right:0;text-align:center;top:163px;font-size:11px}

  .gauge-art{
    position:absolute;left:0;top:0;width:100%;height:100%;
    background:radial-gradient(circle at 50% 48%,#2c2c2e 0%,#1b1b1c 45%,#111 75%);
  }
  .card--gauge .wordmark{left:0;right:0;text-align:center;top:115px;font-size:44px}
  .card--gauge .slogan{left:0;right:0;text-align:center;top:161px;font-size:11px}

  .card--alt .wordmark{left:33px;top:216px;font-size:28px}
  .card--alt .slogan{left:58px;top:247px;font-size:8px}
  .card--alt .phone{right:40px;top:193px}
  .card--alt .email{right:40px;top:217px}
  .card--alt .web{right:40px;top:241px}
</style>
</head>
<body>

<section class="card card--front">
  <div class="wheel-photo" role="img" aria-label="Photo of three alloy car wheels in black, red and dark finishes"></div>
  <div class="wordmark">GearNest</div>
  <div class="slogan">Quality Parts At Affordable Prices</div>
  <div class="holder-name">Rohan Mehtabrooke</div>
  <div class="contact phone"><span class="label">P :</span> 246-555-0192</div>
  <div class="contact email"><span class="label">E :</span> gearnestbb@mailbox-demo.test</div>
  <div class="contact web">www.example-social.test/<b>gearnestbb</b></div>
</section>

<section class="card card--back">
  <div class="band"></div>
  <div class="wordmark">GearNest</div>
  <div class="slogan">Quality Parts At Affordable Prices</div>
</section>

<section class="card card--gauge">
  <div class="gauge-art" role="img" aria-label="Faint illustration of a car instrument cluster with tachometer dial"></div>
  <div class="wordmark">GearNest</div>
  <div class="slogan">Quality Parts At Affordable Prices</div>
</section>

<section class="card card--alt">
  <div class="wheel-photo" role="img" aria-label="Photo of three alloy car wheels in black, red and dark finishes"></div>
  <div class="wordmark">GearNest</div>
  <div class="slogan">Quality Parts At Affordable Prices</div>
  <div class="contact phone"><span class="label">P :</span> 246-555-0192</div>
  <div class="contact email"><span class="label">E :</span> gearnestbb@mailbox-demo.test</div>
  <div class="contact web">www.example-social.test/<b>gearnestbb</b></div>
</section>

</body>
</html>
```